Poster for pawn shop lobby

Looking for green and gold as my colors, like the picture shown of my old poster. This time I'm contemplating with doing pictures as well as just text. Here are ideas of things I buy and give loans on. We want to emphasize jewelry, laptops, game systems, tools. I'm open-minded.
Old & Broken Gold
Jewelry & Collectibles
Diamonds
Video Games & Systems
Up-to-date Computers & Laptops
Tablets
Cameras
Power Tools
Home & Garden Equipment
Sports Equipment
Watches
Antique Collectibles
Musical Instruments
And anything else of value
Shop

```html
<!DOCTYPE html>
<html lang="en">
<head>
<meta charset="utf-8">
<title>Pawn Shop Lobby Poster</title>
<link rel="stylesheet" href="https://fonts.googleapis.com/css2?family=Passion+One:wght@400;700&family=Open+Sans:wght@400&display=swap">
<style>
  :root {
    --olive-gold: #c4ae45;
    --band-yellow: #efd42b;
    --leaf-green: #438200;
    --deep-green: #3a7a00;
    --text-green: #3b7d07;
    --white: #ffffff;
    --cash-tone: #7c8a6a;
    --gold-tone: #a8823c;
  }
  html, body {
    margin: 0;
    padding: 0;
    width: 1200px;
    height: 1000px;
    overflow: hidden;
    background: var(--olive-gold);
  }
  .poster {
    position: relative;
    width: 1200px;
    height: 1000px;
    overflow: hidden;
    background: var(--olive-gold);
    font-family: "Passion One", "Arial Narrow", sans-serif;
  }
  .cash-stack {
    position: absolute;
    left: 0;
    top: 0;
    width: 322px;
    height: 256px;
    background: linear-gradient(160deg, #a9b29a 0%, var(--cash-tone) 55%, #4d5444 100%);
  }
  .top-rule {
    position: absolute;
    left: 0;
    top: 254px;
    width: 1200px;
    height: 14px;
    background: var(--deep-green);
  }
  .headline-band {
    position: absolute;
    left: 0;
    top: 268px;
    width: 1200px;
    height: 184px;
    background: var(--band-yellow);
    display: flex;
    align-items: center;
    justify-content: center;
  }
  .headline {
    margin: 0;
    font-weight: 700;
    font-size: 94px;
    line-height: 1;
    color: var(--text-green);
    letter-spacing: 1px;
    text-shadow: 2px 3px 2px rgba(80, 60, 0, 0.55);
    white-space: nowrap;
    padding-top: 8px;
  }
  .feature-badge {
    position: absolute;
    left: 842px;
    top: -26px;
    width: 306px;
    height: 306px;
    border-radius: 50%;
    background: var(--band-yellow);
    border: 7px solid var(--white);
    box-shadow: 0 4px 8px rgba(0, 0, 0, 0.35);
  }
  .feature-list {
    position: absolute;
    left: 42px;
    top: 82px;
    margin: 0;
    padding: 0;
    list-style: none;
    font-weight: 700;
    font-size: 40px;
    line-height: 47px;
    color: var(--text-green);
    text-shadow: 1px 2px 1px rgba(60, 50, 0, 0.4);
  }
  .panel-left {
    position: absolute;
    left: 0;
    top: 452px;
    width: 626px;
    height: 548px;
    background: var(--olive-gold);
  }
  .panel-right {
    position: absolute;
    left: 626px;
    top: 452px;
    width: 574px;
    height: 548px;
    background: var(--leaf-green);
  }
  .jewelry-photo {
    position: absolute;
    left: 360px;
    top: 455px;
    width: 266px;
    height: 175px;
    border-radius: 40% 10% 45% 55%;
    background: radial-gradient(ellipse at 55% 40%, #e0b86a 0%, var(--gold-tone) 45%, rgba(140, 100, 50, 0) 80%);
  }
  .section-title {
    position: absolute;
    left: 48px;
    top: 474px;
    margin: 0;
    font-weight: 700;
    font-size: 46px;
    line-height: 1;
    color: var(--text-green);
    text-shadow: 1px 2px 1px rgba(60, 50, 0, 0.4);
    padding-bottom: 4px;
    border-bottom: 4px solid var(--deep-green);
    width: 462px;
    white-space: nowrap;
  }
  .item-list {
    position: absolute;
    margin: 0;
    padding: 0;
    list-style: none;
  }
  .item-list li {
    display: flex;
    align-items: center;
    font-weight: 700;
    font-size: 56px;
    line-height: 1;
    color: var(--white);
    text-shadow: 3px 4px 3px rgba(0, 0, 0, 0.45);
    white-space: nowrap;
  }
  .item-list .dollar {
    font-family: "Open Sans", Arial, sans-serif;
    font-weight: 400;
    font-size: 50px;
    line-height: 1;
    margin-right: 6px;
  }
  .item-list .dollar.spaced {
    margin-right: 16px;
  }
  .item-list .amp {
    font-family: "Open Sans", Arial, sans-serif;
    font-weight: 400;
    margin: 0 8px;
  }
  .items-left {
    left: 34px;
    top: 547px;
  }
  .items-left li {
    height: 87px;
  }
  .items-right {
    left: 656px;
    top: 456px;
  }
  .items-right li {
    height: 78px;
    font-size: 50px;
  }
</style>
</head>
<body>
  <main class="poster">
    <div class="cash-stack" role="img" aria-label="Photo of stacked bundles of hundred-dollar bills"></div>

    <div class="top-rule"></div>

    <div class="headline-band">
      <h1 class="headline">we'll loan or pay you cash!</h1>
    </div>

    <div class="feature-badge">
      <ul class="feature-list">
        <li>jewerly</li>
        <li>laptops</li>
        <li>game systems</li>
        <li>tools</li>
      </ul>
    </div>

    <section class="panel-left"></section>
    <section class="panel-right"></section>

    <div class="jewelry-photo" role="img" aria-label="Photo of a pile of gold chains, rings and jewelry"></div>

    <h2 class="section-title">buy and give loans</h2>

    <ul class="item-list items-left">
      <li><span class="dollar">$</span>gold jewerly<span class="amp">&amp;</span>coins</li>
      <li><span class="dollar">$</span>scrap gold</li>
      <li><span class="dollar">$</span>diamonds</li>
      <li><span class="dollar spaced">$</span>estates</li>
      <li><span class="dollar spaced">$</span>platinum</li>
    </ul>

    <ul class="item-list items-right">
      <li><span class="dollar">$</span>silver</li>
      <li><span class="dollar spaced">$</span>old<span class="amp">&amp;</span>luxury watches</li>
      <li><span class="dollar">$</span>camera equipments</li>
      <li><span class="dollar">$</span>computers</li>
      <li><span class="dollar">$</span>military</li>
      <li><span class="dollar">$</span>musical instruments</li>
      <li><span class="dollar spaced">$</span>collectibles/ toys</li>
    </ul>
  </main>
</body>
</html>
```